Flyer for rhytmic gymnastics school

Hello everybody. We are planning to launch advertising campaign for our rhytmic gymnastics school. The flyers will be distributed directly to people throughout the city putting them on doorknobs. So the design should be very attractive and clear. Our goal is to attract small girls age 3-5. The idea and concept of the flyer is up to you but we just want to empasize the attractivness and benefits of this sport - basically it's a combination of ballet, gymnastics and dance. We even consider using cartoonish style of the flyer. We also have our logo, it's attached. The school is located in Southern California, with a diverse population. Chinese and Korean families that recently came to the US probably will be the main target audience since they know about this sport more. So one the goals is to show people who have never heard about Rhytmic Gymnastics what this sport is about. We need to design both sides of the flyers. We think that on one side of the flyer should be placed photo of our school (it should be ready in two days) and information about facility, adress etc. And as I mentioned one side should be creative and unusual to attract kids and parents. Here is some information about VP in general

Looking for new sport for your daughter?
Try Rhythmic Gymnastics! It’s an Olympic Sport!

• Enrollment is now open for Girls 3, 5-5 year old
• Competitive opportunity or recreational classes
• Instruction based on Russian School of Rhythmic Gymnastics
• A team of professional coaches
Brand new facility exlusively for rhytmic gymnastics activity
FREE introductory class!

Rhythmic Gymnastics is a discipline combining grace, coordination, agility and
artistry.
Rhythmic gymnastics combines ballet and creative movements to music, while
working with ribbons, balls, hoops, ropes and clubs in a choreographed danceand-tumble routine. Rhythmic gymnastics creates beautiful strong bodies as well
as improving child’s cognitive abilities

Requirements
Must have
• We see the flyer as a double sided flat A6 size, but again it's up to you.
Location
41876 Marlow Crest dr
Laguna Hills, CA
92653
www.vendapoise.us
Phone # 555 382 4106
e-mail kids@vendapoise.us
Facebook page https://www.facebook.com/TolvaRhythmicGymnastics

```html
<!DOCTYPE html>
<html lang="en">
<head>
<meta charset="utf-8">
<title>Venda Poise School of Rhythmic Gymnastics – Flyer</title>
<link rel="stylesheet" href="https://fonts.googleapis.com/css2?family=EB+Garamond:ital,wght@0,400;0,500;0,700;1,600;1,700&display=swap">
<style>
  :root {
    --navy: #2b2a78;
    --red: #dd2a26;
    --crimson: #c8232c;
    --magenta: #e0237a;
    --ink: #1a1a1a;
    --paper: #ffffff;
  }
  * { margin: 0; padding: 0; box-sizing: border-box; }
  html, body { width: 852px; height: 1200px; overflow: hidden; background: var(--paper); }
  .flyer {
    position: relative;
    width: 852px;
    height: 1200px;
    overflow: hidden;
    background: var(--paper);
    font-family: "EB Garamond", Georgia, serif;
    color: var(--ink);
  }
  .backdrop { position: absolute; inset: 0; width: 852px; height: 1200px; z-index: 0; }

  .intro {
    position: absolute;
    z-index: 2;
    left: 48px;
    top: 30px;
    width: 764px;
    font-size: 20.5px;
    line-height: 27px;
    text-align: justify;
    color: var(--paper);
  }
  .intro strong { font-weight: 700; }
  .intro .tail { display: block; text-align: left; }

  .brand {
    position: absolute;
    z-index: 2;
    left: 590px;
    top: 222px;
    width: 230px;
    display: flex;
    align-items: center;
    gap: 12px;
  }
  .brand-dot { width: 16px; height: 16px; border-radius: 50%; background: var(--magenta); flex: none; }
  .brand-name {
    font-size: 26px;
    line-height: 30px;
    font-weight: 500;
    color: var(--magenta);
  }

  .headline {
    position: absolute;
    z-index: 3;
    left: 0;
    top: 360px;
    width: 852px;
    height: 180px;
    font-style: italic;
    font-weight: 700;
    color: var(--navy);
    line-height: 1;
  }
  .headline span { display: block; position: absolute; white-space: nowrap; }
  .headline .l1 { left: 165px; top: 0; font-size: 72px; }
  .headline .l2 { left: 304px; top: 60px; font-size: 60px; }
  .headline .l3 { left: 206px; top: 118px; font-size: 57px; }

  .tagline {
    position: absolute;
    z-index: 2;
    color: var(--crimson);
    font-size: 44px;
    font-weight: 500;
    line-height: 1;
    white-space: nowrap;
  }
  .tagline.t1 { left: 126px; top: 580px; }
  .tagline.t2 { left: 233px; top: 642px; }

  .benefits {
    position: absolute;
    z-index: 2;
    left: 452px;
    top: 708px;
    list-style: none;
    font-size: 21px;
    font-weight: 700;
    line-height: 27px;
    color: var(--ink);
  }
  .benefits li { position: relative; padding-left: 14px; }
  .benefits li::before {
    content: "";
    position: absolute;
    left: 0;
    top: 11px;
    width: 6px;
    height: 6px;
    border-radius: 50%;
    background: var(--ink);
  }

  .gymnast-art {
    position: absolute;
    z-index: 1;
    left: 40px;
    top: 760px;
    width: 330px;
    height: 420px;
    border-radius: 46% 54% 40% 60% / 40% 40% 60% 60%;
    background: radial-gradient(ellipse at 45% 45%, var(--magenta) 0%, #f4a3c8 45%, rgba(246, 211, 182, 0.6) 70%, rgba(255,255,255,0) 80%);
  }

  .offer {
    position: absolute;
    z-index: 2;
    left: 396px;
    top: 1004px;
    font-size: 28px;
    font-weight: 700;
    line-height: 41px;
    color: var(--paper);
  }
</style>
</head>
<body>
<main class="flyer">
  <svg class="backdrop" viewBox="0 0 852 1200" aria-hidden="true">
    <defs>
      <linearGradient id="footer-blend" x1="0" y1="0" x2="1" y2="0">
        <stop offset="0" stop-color="#2b2a78"/>
        <stop offset="0.45" stop-color="#8a2560"/>
        <stop offset="1" stop-color="#dd2a26"/>
      </linearGradient>
    </defs>
    <rect class="top-red" x="0" y="0" width="852" height="520" fill="var(--red)"/>
    <rect class="top-navy" x="0" y="0" width="295" height="420" fill="var(--navy)"/>
    <path class="white-sweep" d="M0 290 C 180 200, 520 150, 852 215 L 852 1200 L 0 1200 Z" fill="var(--paper)"/>
    <path class="navy-wave" d="M0 268 C 60 300, 120 420, 200 470 C 120 440, 50 380, 0 350 Z" fill="var(--navy)"/>
    <path class="red-crescent" d="M250 585 C 470 570, 690 520, 852 460 L 852 530 C 700 560, 480 580, 250 585 Z" fill="var(--red)"/>
    <path class="footer-band" d="M0 1075 C 180 1090, 300 1000, 520 960 C 660 935, 760 925, 852 915 L 852 1200 L 0 1200 Z" fill="url(#footer-blend)"/>
  </svg>

  <p class="intro"><strong>Rhythmic Gymnastics</strong> is a discipline combining grace, coordination, agility and artistry. Rhythmic gymnastics combines ballet and creative movements to music, while working with ribbons, balls, hoops, ropes and clubs in a choreographed dance and-tumble routine. Rhythmic gymnastics creates beautiful strong bodies as well as improving<span class="tail">child’s cognitive<br>abilities</span></p>

  <div class="brand">
    <span class="brand-dot"></span>
    <span class="brand-name">Venda Poise School of Rhythmic Gymnastics</span>
  </div>

  <h1 class="headline">
    <span class="l1">Looking for</span>
    <span class="l2">new sport</span>
    <span class="l3">for your daughter?</span>
  </h1>

  <p class="tagline t1">Try Rhythmic Gymnastics!</p>
  <p class="tagline t2">It’s an Olympic Sport!</p>

  <ul class="benefits">
    <li>Enrollment is now open for<br>Girls 3, 5-5 year old</li>
    <li>Competitive opportunity or<br>recreational classes</li>
    <li>Instruction based on Russian<br>School of Rhythmic Gymnastics</li>
    <li>A team of professional coaches</li>
  </ul>

  <div class="gymnast-art" role="img" aria-label="Cartoon girl in a pink leotard leaping with a red ribbon"></div>

  <p class="offer">Brand new facility<br>exlusively for<br>rhytmic gymnastics activity<br>FREE introductory class!</p>
</main>
</body>
</html>
```